" Trabalhamos visitando nossos clientes no porta a portas, clientes esses com escolas, colégios e creches particulares e prefeituras. Fora a venda particular, participamos de licitações em prefeituras. "

```html
<!DOCTYPE html>
<html lang="pt-BR">
<head>
<meta charset="UTF-8">
<title>Nova Prima Comercial — Cartão de visita</title>
<link href="https://fonts.googleapis.com/css2?family=Montserrat:wght@400;500;600&display=swap" rel="stylesheet">
<style>
  :root{
    --bg:#e9eaec;
    --card-dark:#1f252b;
    --card-light:#f6f6f4;
    --gold:#c9a24a;
    --gold-deep:#a98332;
    --ink:#2b2f33;
    --muted:#6d7176;
    --text-light:#e8e6e1;
  }
  *{box-sizing:border-box;margin:0;padding:0}
  html,body{width:1200px;height:1200px;overflow:hidden}
  body{
    background:var(--bg);
    font-family:"Montserrat",sans-serif;
    display:flex;flex-direction:column;align-items:center;justify-content:center;gap:60px;
  }
  .card{
    width:840px;height:480px;position:relative;overflow:hidden;
    box-shadow:0 18px 40px rgba(0,0,0,.18);
  }
  /* Front (dark) */
  .card--front{background:var(--card-dark);color:var(--text-light)}
  .front__block{
    position:absolute;left:0;top:120px;width:230px;height:230px;
    background:linear-gradient(135deg,var(--gold),var(--gold-deep));
  }
  .brand{
    position:absolute;display:flex;flex-direction:column;align-items:center;
  }
  .brand__name{
    font-weight:500;color:var(--gold);letter-spacing:.08em;text-transform:uppercase;line-height:1;
  }
  .brand__tag{
    font-weight:400;text-transform:uppercase;letter-spacing:.5em;margin-top:8px;
  }
  .card--front .brand{left:380px;top:64px}
  .card--front .brand__name{font-size:34px}
  .card--front .brand__tag{font-size:10px;color:var(--gold)}
  .contacts{position:absolute;left:380px;top:160px;list-style:none}
  .contacts li{display:flex;align-items:center;gap:14px;font-size:14px;letter-spacing:.03em;height:38px}
  .icon{
    width:26px;height:26px;border-radius:50%;background:var(--gold);
    display:flex;align-items:center;justify-content:center;flex:none;
  }
  .icon svg{width:14px;height:14px;fill:none;stroke:var(--card-dark);stroke-width:2;stroke-linecap:round;stroke-linejoin:round}
  .address{position:absolute;left:380px;top:318px;display:flex;gap:10px;font-size:12.5px;line-height:1.5;letter-spacing:.03em;text-transform:uppercase}
  .address svg{width:16px;height:18px;flex:none;margin-top:1px;fill:var(--gold)}
  /* Back (light) */
  .card--back{background:var(--card-light)}
  .card--back .brand{left:0;right:0;top:200px}
  .card--back .brand__name{font-size:64px}
  .card--back .brand__tag{font-size:14px;color:var(--muted);margin-top:14px}
</style>
</head>
<body>
  <section class="card card--front" aria-label="Frente do cartão">
    <div class="front__block"></div>
    <div class="brand">
      <span class="brand__name">Nova Prima</span>
      <span class="brand__tag">Comercial</span>
    </div>
    <ul class="contacts">
      <li><span class="icon"><svg viewBox="0 0 24 24"><path d="M5 3h4l2 5-2.5 1.5a11 11 0 0 0 6 6L16 13l5 2v4a2 2 0 0 1-2 2A16 16 0 0 1 3 5a2 2 0 0 1 2-2z"/></svg></span>(11) 94120-3378 | 94120-5516</li>
      <li><span class="icon"><svg viewBox="0 0 24 24"><rect x="3" y="5" width="18" height="14" rx="2"/><path d="M3 7l9 6 9-6"/></svg></span>CONTATO@NOVAPRIMA.COM.BR</li>
      <li><span class="icon"><svg viewBox="0 0 24 24"><circle cx="12" cy="12" r="9"/><path d="M3 12h18M12 3a14 14 0 0 1 0 18M12 3a14 14 0 0 0 0 18"/></svg></span>NOVAPRIMA.COM.BR</li>
    </ul>
    <div class="address">
      <svg viewBox="0 0 24 28"><path d="M12 0a9 9 0 0 0-9 9c0 7 9 19 9 19s9-12 9-19a9 9 0 0 0-9-9zm0 13a4 4 0 1 1 0-8 4 4 0 0 1 0 8z"/></svg>
      <p>Rua das Acácias, 120,<br>Bairro Jardim Sul, Salas 201 e 202<br>Complemento: Centro Empresarial Aurora<br>CEP: 12.345-678</p>
    </div>
  </section>

  <section class="card card--back" aria-label="Verso do cartão">
    <div class="brand">
      <span class="brand__name">Nova Prima</span>
      <span class="brand__tag">Comercial</span>
    </div>
  </section>
</body>
</html>
```